hobby beef jerky maker looking to break into the commercial market

We need product labels designed for each flavour of jerky we make. Currently have 3 flavours that we are ready to share with the world. We need in your face designs to help us stand out from an already crowded market.
The product name is Rowdy Beef Jerky.
The flavours we offer have been named Porch Party, Tangy Glow and Fiery Bite.
The Rowdy Beef Jerky Title should remain the same across the three labels but the design for each flavour can change as you see fit.
Label needs to fit within 110mm x 110mm to suit our current packaging

Industry/Entity Type

Food Production

Logo Text

Morvathen Clover

Colors

Designer to choose colors to be used in the design.

Requirements
Must have
• "Rowdy Beef Jerky" font and colour must remain the same across the 3 designs
Nice to have
• The labels will be used on the clear side of the packaging with a small space towards the bottom being left visible so the product inside can be seen

```html
<!DOCTYPE html>
<html lang="en">
<head>
<meta charset="utf-8">
<title>Rowdy Beef Jerky – Fiery Bite Label</title>
<link rel="stylesheet" href="https://fonts.googleapis.com/css2?family=Archivo+Black&family=Open+Sans:wght@300;400;600;700&family=Open+Sans+Condensed:wght@700&display=swap">
<style>
  :root {
    --page: #ffffff;
    --label-red: #a01529;
    --gold: #d4ad52;
    --gold-light: #f3d98a;
    --gold-dark: #a9812b;
    --panel-dark: #140606;
    --badge-maroon: #5a0f16;
    --accent-red: #c8101e;
    --flavour-red: #ec2130;
    --tagline-orange: #f28a1a;
    --white: #ffffff;
  }
  * { margin: 0; padding: 0; box-sizing: border-box; }
  html, body { width: 1200px; height: 1000px; overflow: hidden; background: var(--page); }
  .canvas { position: relative; width: 1200px; height: 1000px; }
  .label {
    position: absolute; left: 173px; top: 72px; width: 855px; height: 857px;
    background: var(--label-red);
    border: 5px solid var(--gold);
  }
  .frame { position: absolute; left: 0; top: 0; width: 1200px; height: 1000px; }
  .bull-emblem {
    position: absolute; left: 497px; top: 240px; width: 205px; height: 128px;
    background: radial-gradient(ellipse at 50% 55%, var(--accent-red) 0%, #8e0c17 100%);
    border-radius: 40px 40px 60px 60px;
  }
  .brand {
    position: absolute; left: 0; width: 1200px; text-align: center;
    font-family: "Archivo Black", sans-serif; line-height: 1;
  }
  .brand-name {
    top: 365px; font-size: 112px; letter-spacing: 1px;
    background: linear-gradient(180deg, var(--gold-light) 0%, var(--gold) 45%, var(--gold-dark) 100%);
    -webkit-background-clip: text; background-clip: text; color: transparent;
  }
  .brand-product { top: 484px; font-size: 84px; color: var(--white); letter-spacing: 1px; }
  .tagline {
    position: absolute; left: 0; width: 1200px; top: 603px; text-align: center;
    font-family: "Open Sans", sans-serif; font-weight: 300; font-size: 42px;
    color: var(--tagline-orange); letter-spacing: 1px;
  }
  .flavour-bar {
    position: absolute; left: 178px; top: 787px; width: 633px; height: 79px;
    background: var(--panel-dark);
    border: 3px solid var(--accent-red);
    border-left-color: #f2d21c; border-top-color: #e0a020;
    border-radius: 0 12px 12px 0;
    display: flex; align-items: center; padding-left: 40px;
  }
  .flavour-name {
    font-family: "Open Sans", sans-serif; font-weight: 600; font-size: 44px;
    color: var(--flavour-red); letter-spacing: 0.5px; white-space: nowrap;
  }
  .net-weight {
    position: absolute; left: 878px; top: 800px; width: 118px; height: 94px;
    border: 3px solid var(--white); border-radius: 34px 34px 0 0;
    display: flex; align-items: center; justify-content: center;
    font-family: "Open Sans Condensed", "Open Sans", sans-serif; font-weight: 700;
    font-size: 40px; color: var(--white);
  }
</style>
</head>
<body>
<main class="canvas">
  <div class="label"></div>

  <svg class="frame" viewBox="0 0 1200 1000" aria-hidden="true">
    <defs>
      <linearGradient id="goldStroke" x1="0" y1="0" x2="0" y2="1">
        <stop offset="0" stop-color="#f3d98a"/>
        <stop offset="0.5" stop-color="#d4ad52"/>
        <stop offset="1" stop-color="#a9812b"/>
      </linearGradient>
      <path id="plaque" d="M255 298 H325 Q360 282 405 280 Q602 205 800 280 Q845 282 880 298 H950 V355 Q988 420 988 482 Q988 545 950 607 V665 H880 Q845 682 800 685 Q602 758 405 685 Q360 682 325 665 H255 V607 Q217 545 217 482 Q217 420 255 355 Z"/>
    </defs>
    <use href="#plaque" fill="none" stroke="#d4ad52" stroke-width="2.5"
         transform="translate(602 482) scale(1.055 1.07) translate(-602 -482)"/>
    <use href="#plaque" fill="#140606" stroke="url(#goldStroke)" stroke-width="9"/>

    <g class="quality-badge">
      <circle cx="910" cy="168" r="78" fill="#5a0f16" stroke="#d4ad52" stroke-width="3"/>
      <circle cx="910" cy="158" r="50" fill="url(#goldStroke)" stroke="#f3d98a" stroke-width="2"/>
      <path d="M815 205 L830 212 L828 195 Z M1005 205 L990 212 L992 195 Z" fill="#5a0f16" stroke="#d4ad52" stroke-width="1.5"/>
      <rect x="828" y="188" width="164" height="34" rx="4" fill="#5a0f16" stroke="#d4ad52" stroke-width="2"/>
    </g>
  </svg>

  <div class="bull-emblem" role="img" aria-label="Red stylised bull head emblem"></div>

  <h1>
    <span class="brand brand-name">ROWDY</span>
    <span class="brand brand-product">BEEF JERKY</span>
  </h1>
  <p class="tagline">THE TRUE TASTE</p>

  <div class="flavour-bar"><span class="flavour-name">FIERY BITE FLAVOUR</span></div>
  <div class="net-weight">00 g</div>
</main>
</body>
</html>
```